Redesign our iOS App Design mockups

- Redesign our current Veltro App Mockup
- Keep the design simple so that programmers do not have to do too much extra work to make your design work.
- Look at the attached website screenshot for the overall look and feel, and color scheme
- Convert the attached vector logo to iOS Icon format.
- Deliver all graphics in the density required for Veltro QL Prime.
- I have attached the current iOS mockup in a .ZIP file but you can view it here as well: https://boards.mockvault.net/share/QWTRPL8HNB2

Target Market(s)

Mostly Male Internet Consumers between the ages of 20 and 35

Industry/Entity Type

Internet

Colors

Designer to choose colors to be used in the design.

Requirements
Must have
• - Deliver all graphics in the density required for Veltro QL Prime
• - Should also look good on Tabrix and Tabrix pro
• - Design type should be “FLAT.”
• - Spell out fonts used in the design and where they are used. Also, include font sizes.
• - Please use ALL the elements in each page and use all placements and text EXACTLY. Please do not improvise with text or components.
• I have designed the mockup exactly the way I like it. I just want it to made to look better.
Should not have

```html
<!DOCTYPE html>
<html lang="en">
<head>
<meta charset="utf-8">
<title>Login Screen</title>
<link rel="stylesheet" href="https://fonts.googleapis.com/css2?family=Montserrat:wght@300;400;500;600;700&display=swap">
<style>
  :root {
    --page-bg: #101010;
    --coral-light: #f6614f;
    --coral-mid: #ea5241;
    --coral-deep: #d84234;
    --ink: #111111;
    --white: #ffffff;
    --field-icon: #e9503f;
    --muted-grey: #a8a8a8;
    --divider: rgba(120, 30, 20, 0.35);
    --text-light: rgba(255, 255, 255, 0.92);
  }
  * { box-sizing: border-box; margin: 0; padding: 0; }
  html, body {
    width: 1200px;
    height: 1200px;
    overflow: hidden;
    background: var(--page-bg);
    font-family: "Montserrat", sans-serif;
  }
  .app-screen {
    position: absolute;
    left: 341px;
    top: 39px;
    width: 518px;
    height: 1122px;
    border-radius: 48px;
    overflow: hidden;
    background: linear-gradient(200deg, var(--coral-light) 0%, var(--coral-mid) 45%, var(--coral-deep) 100%);
  }
  .status-time {
    position: absolute;
    left: 40px;
    top: 18px;
    font-size: 18px;
    font-weight: 600;
    color: var(--ink);
  }
  .status-icons {
    position: absolute;
    right: 22px;
    top: 20px;
    display: flex;
    gap: 6px;
    align-items: center;
  }
  .nav-title {
    position: absolute;
    top: 72px;
    width: 100%;
    text-align: center;
    font-size: 28px;
    font-weight: 600;
    color: var(--ink);
  }
  .nav-divider {
    position: absolute;
    top: 124px;
    left: 0;
    width: 100%;
    height: 1px;
    background: var(--divider);
  }
  .world-backdrop {
    position: absolute;
    top: 110px;
    left: 0;
    width: 100%;
    height: 380px;
    background: radial-gradient(ellipse at 50% 45%, rgba(255, 255, 255, 0.07) 0%, rgba(255, 255, 255, 0.02) 60%, rgba(255, 255, 255, 0) 80%);
  }
  .brand-mark {
    position: absolute;
    left: 50%;
    top: 212px;
    width: 120px;
    height: 120px;
    margin-left: -60px;
    border-radius: 50%;
    background: var(--white);
  }
  .brand-name {
    position: absolute;
    top: 376px;
    width: 100%;
    text-align: center;
    font-size: 42px;
    font-weight: 700;
    letter-spacing: -1px;
    color: var(--ink);
  }
  .field-label {
    position: absolute;
    left: 64px;
    font-size: 22px;
    font-weight: 600;
    color: var(--ink);
  }
  .label-user { top: 482px; }
  .label-pass { top: 591px; }
  .text-field {
    position: absolute;
    left: 65px;
    width: 387px;
    height: 50px;
    background: var(--white);
    display: flex;
    align-items: center;
    padding: 0 14px;
  }
  .field-user { top: 520px; }
  .field-pass { top: 629px; }
  .field-icon { width: 22px; flex: none; }
  .field-value {
    margin-left: 14px;
    font-size: 19px;
    font-weight: 600;
    color: var(--ink);
    display: flex;
    align-items: center;
  }
  .caret {
    display: inline-block;
    width: 1px;
    height: 30px;
    margin-left: 3px;
    background: var(--field-icon);
  }
  .field-masked {
    margin-left: 14px;
    font-size: 14px;
    letter-spacing: 1px;
    color: var(--muted-grey);
  }
  .field-clear { position: absolute; right: 10px; }
  .options-row {
    position: absolute;
    left: 65px;
    top: 703px;
    width: 387px;
    display: flex;
    justify-content: space-between;
    align-items: center;
    font-size: 17px;
    font-weight: 300;
    color: var(--text-light);
  }
  .remember-me { display: flex; align-items: center; gap: 14px; }
  .forgot-link {
    font-style: italic;
    text-decoration: underline;
    color: var(--text-light);
  }
  .login-button {
    position: absolute;
    left: 65px;
    top: 779px;
    width: 387px;
    height: 56px;
    border-radius: 28px;
    background: var(--ink);
    color: var(--white);
    font-size: 20px;
    font-weight: 600;
    display: flex;
    align-items: center;
    justify-content: center;
  }
  .signup-prompt {
    position: absolute;
    top: 1025px;
    width: 100%;
    text-align: center;
    font-size: 17px;
    font-weight: 300;
    color: var(--text-light);
  }
  .signup-link {
    font-weight: 500;
    color: var(--white);
    text-decoration: underline;
  }
  .home-indicator {
    position: absolute;
    left: 149px;
    top: 1091px;
    width: 220px;
    height: 5px;
    border-radius: 3px;
    background: var(--ink);
  }
</style>
</head>
<body>
<main class="app-screen">
  <div class="status-time">9:41</div>
  <div class="status-icons">
    <svg width="22" height="14" viewBox="0 0 22 14" aria-hidden="true">
      <rect x="0" y="9" width="4" height="5" rx="1" fill="#111"/>
      <rect x="6" y="6" width="4" height="8" rx="1" fill="#111"/>
      <rect x="12" y="3" width="4" height="11" rx="1" fill="#111"/>
      <rect x="18" y="0" width="4" height="14" rx="1" fill="#111"/>
    </svg>
    <svg width="19" height="14" viewBox="0 0 19 14" aria-hidden="true">
      <path d="M1 5 A12 12 0 0 1 18 5" stroke="#111" stroke-width="2.4" fill="none" stroke-linecap="round"/>
      <path d="M4.5 8.5 A7 7 0 0 1 14.5 8.5" stroke="#111" stroke-width="2.4" fill="none" stroke-linecap="round"/>
      <circle cx="9.5" cy="12" r="2" fill="#111"/>
    </svg>
    <svg width="30" height="14" viewBox="0 0 30 14" aria-hidden="true">
      <rect x="1" y="1" width="25" height="12" rx="3" stroke="#111" stroke-width="1.5" fill="none"/>
      <rect x="3" y="3" width="21" height="8" rx="1.5" fill="#111"/>
      <rect x="27.5" y="5" width="2" height="4" rx="1" fill="#111"/>
    </svg>
  </div>

  <h1 class="nav-title">Login</h1>
  <div class="nav-divider"></div>

  <div class="world-backdrop" role="img" aria-label="Faint dotted world map backdrop"></div>
  <div class="brand-mark"></div>
  <div class="brand-name">COZYNET</div>

  <div class="field-label label-user">User ID:</div>
  <div class="text-field field-user">
    <svg class="field-icon" viewBox="0 0 22 16" height="16" aria-hidden="true">
      <rect x="0" y="0" width="22" height="16" rx="2" fill="#e9503f"/>
      <path d="M1.5 2 L11 9 L20.5 2" stroke="#fff" stroke-width="2" fill="none"/>
    </svg>
    <span class="field-value">email@example.com<span class="caret"></span></span>
    <svg class="field-clear" width="17" height="17" viewBox="0 0 17 17" aria-hidden="true">
      <circle cx="8.5" cy="8.5" r="8.5" fill="#b0b0b0"/>
      <path d="M5.5 5.5 L11.5 11.5 M11.5 5.5 L5.5 11.5" stroke="#fff" stroke-width="1.6"/>
    </svg>
  </div>

  <div class="field-label label-pass">Password:</div>
  <div class="text-field field-pass">
    <svg class="field-icon" viewBox="0 0 18 24" height="24" aria-hidden="true">
      <path d="M4 10 V6.5 A5 5 0 0 1 14 6.5 V10" stroke="#e9503f" stroke-width="2.6" fill="none"/>
      <rect x="0" y="10" width="18" height="14" rx="2" fill="#e9503f"/>
      <rect x="8" y="15" width="2" height="5" rx="1" fill="#fff"/>
    </svg>
    <span class="field-masked">*************</span>
  </div>

  <div class="options-row">
    <span class="remember-me">
      <svg width="16" height="16" viewBox="0 0 16 16" aria-hidden="true">
        <rect x="0.75" y="0.75" width="14.5" height="14.5" stroke="#111" stroke-width="1.5" fill="none"/>
        <path d="M3.5 8 L6.5 11 L12.5 4.5" stroke="#111" stroke-width="1.6" fill="none"/>
      </svg>
      Remember me
    </span>
    <span class="forgot-link">Forgot Password?</span>
  </div>

  <div class="login-button">LOGIN NOW</div>

  <p class="signup-prompt">Don’t have an account yet? <span class="signup-link">Sign Up</span> here.</p>

  <div class="home-indicator"></div>
</main>
</body>
</html>
```